Tablet App design for business management system

TaskOra is a business management system made especially for service based businesses (our subscribers). It enables systemising your service businesses. This can be used by diverse industries like automotive service, beauty (hair salons, nail spas), Spas, Chiropractor, acupuntcure, osteo, yoga studio, business coach, etc.

The UI of the app needs to be designed using flat and clean UI design trends that are currently prevailing for B2C apps. Even the sliding menu panel can be removed and alternative placement of this functionality can be suggested. The color palette used for the design should be limited (3-5 colours)

The Current UI screens are open to suggestions for change. For ease of management in minimum steps, consolidation of functionality on different screens can be suggested, accompanies by a rational reason with the objective of having a simple and straight forward user experience.

User should be able to move from one function to another (booking > view appointments > profile) in no more than 1 or max 2 gestures.

Target Market(s)

SME businesses that provide time based services

Industry/Entity Type

Business

Font styles to use
Sans Serif

Requirements
Must have
• The power point slides give a detailed account of the process flow and functionality that the app is to follow.
• Reference this slide to ensure that your final design must have all screens that are required to deliver the functionality.

```html
<!DOCTYPE html>
<html lang="en">
<head>
<meta charset="utf-8">
<title>TaskOra – Client Contact</title>
<link href="https://fonts.googleapis.com/css2?family=Roboto:wght@400;500&display=swap" rel="stylesheet">
<style>
:root{
  --green:#5aae7f;
  --indigo:#3f51b5;
  --cyan:#7fdcf3;
  --text:#5f6466;
  --icon:#7d8284;
  --heading:#3a4040;
  --field:rgba(250,250,248,.62);
  --tab:rgba(244,244,242,.86);
  --divider:rgba(0,0,0,.09);
}
*{box-sizing:border-box;margin:0;padding:0}
html,body{width:1200px;height:900px;overflow:hidden}
body{
  position:relative;font-family:'Roboto',sans-serif;color:var(--text);
  background:linear-gradient(160deg,#c9d9d0 0%,#dfe4dc 30%,#e8e6df 55%,#c9d8cf 75%,#b6cfcb 100%);
}
.tint{position:absolute;inset:250px 0 0 0;
  background:radial-gradient(ellipse at 100% 0%,rgba(250,214,200,.55),transparent 45%),
             radial-gradient(ellipse at 0% 60%,rgba(160,200,180,.35),transparent 50%);}
.hero{position:absolute;left:0;top:0;width:1200px;height:250px;
  background:radial-gradient(ellipse at 30% 40%,#6f7f62 0%,transparent 40%),
             radial-gradient(ellipse at 80% 50%,#7fc6a2 0%,transparent 45%),
             linear-gradient(180deg,#3f7a5e 0%,#5d9477 60%,#708f80 100%);}
.status{position:absolute;top:0;left:0;width:1200px;height:38px;color:#fff;font-size:16px;font-weight:500}
.status .carrier{position:absolute;left:18px;top:10px;display:flex;align-items:center;gap:8px}
.status .time{position:absolute;left:0;right:0;top:10px;text-align:center}
.status .battery{position:absolute;right:18px;top:10px;display:flex;align-items:center;gap:8px}
.avatar{position:absolute;left:544px;top:56px;width:112px;height:112px;border-radius:50%;
  background:radial-gradient(circle at 50% 45%,#d9a98e,#8f5a3c 75%);}
.edit-badge{position:absolute;left:636px;top:70px;width:21px;height:21px;border-radius:50%;background:#d6141c;border:2px solid #fff}
.client-name{position:absolute;left:0;right:0;top:177px;text-align:center;color:#fff;font-size:20px}
.client-phone{position:absolute;left:0;right:0;top:206px;text-align:center;color:var(--cyan);font-size:15px}
.update-btn{position:absolute;left:1005px;top:182px;width:168px;height:42px;background:var(--indigo);color:#fff;
  font-size:16px;letter-spacing:.5px;display:flex;align-items:center;justify-content:center;gap:14px;
  box-shadow:2px 2px 3px rgba(0,0,0,.3)}
.tabs{position:absolute;left:0;top:250px;width:1200px;height:63px;display:flex}
.tab{flex:1;display:flex;align-items:center;justify-content:center;gap:12px;font-size:21px;color:#3d4244;
  background:var(--tab);border-left:1px solid var(--divider)}
.tab.active{background:var(--green);color:#fff;border:none}
.field{position:absolute;height:69px;background:var(--field);display:flex;align-items:center;
  box-shadow:0 1px 2px rgba(0,0,0,.08)}
.field .ico{width:77px;height:44px;display:flex;align-items:center;justify-content:center;border-right:1px solid var(--divider)}
.field .label{padding-left:21px;font-size:18px}
.section-title{position:absolute;left:19px;top:732px;font-size:21px;color:var(--heading)}
svg.i{fill:none;stroke:var(--icon);stroke-width:1.6}
</style>
</head>
<body>
<div class="tint"></div>
<div class="hero" role="img" aria-label="Soft blurred green outdoor backdrop"></div>

<div class="status">
  <div class="carrier">Tablet
    <svg width="16" height="12" viewBox="0 0 16 12"><path d="M1 4a10 10 0 0 1 14 0M3.5 6.5a6.5 6.5 0 0 1 9 0M6 9a3 3 0 0 1 4 0" stroke="#fff" stroke-width="1.8" fill="none"/><circle cx="8" cy="11" r="1" fill="#fff"/></svg>
  </div>
  <div class="time">4:21 PM</div>
  <div class="battery">
    <svg width="10" height="16" viewBox="0 0 10 16"><path d="M1 4l8 8-4 3V1l4 3-8 8" stroke="#cfe" stroke-width="1.2" fill="none"/></svg>
    100%
    <svg width="38" height="16" viewBox="0 0 38 16"><rect x="1" y="1" width="33" height="14" rx="3" stroke="#fff" fill="none"/><rect x="3" y="3" width="29" height="10" rx="1.5" fill="#fff"/><rect x="35" y="5" width="2" height="6" fill="#fff"/></svg>
  </div>
</div>

<div class="avatar" role="img" aria-label="Client profile photo"></div>
<div class="edit-badge">
  <svg width="17" height="17" viewBox="0 0 17 17"><path d="M5 12l1-3 5-5 2 2-5 5z" fill="#fff"/></svg>
</div>
<div class="client-name">Lena Hartwell</div>
<div class="client-phone">04 555 010 2287</div>
<div class="update-btn">UPDATE
  <svg width="22" height="22" viewBox="0 0 22 22" fill="none" stroke="#fff" stroke-width="1.6"><path d="M5 5a8 8 0 0 0 4 14M17 17a8 8 0 0 0-4-14"/><path d="M9 15v4H5M13 7V3h4"/></svg>
</div>

<nav class="tabs">
  <div class="tab active">
    <svg width="20" height="16" viewBox="0 0 20 16" fill="none" stroke="#fff" stroke-width="1.4"><rect x="1" y="1" width="18" height="14"/><circle cx="6" cy="6" r="2"/><path d="M3 12c0-3 6-3 6 0M11 5h6M11 8h6M11 11h6"/></svg>Contact</div>
  <div class="tab">
    <svg width="22" height="22" viewBox="0 0 22 22" fill="none" stroke="#3d4244" stroke-width="1.5"><path d="M4 6a9 9 0 1 0 3-3"/><path d="M3 2v4h4"/><text x="6.5" y="14" font-size="7" fill="#3d4244" stroke="none" font-family="Roboto,sans-serif">24</text></svg>Service</div>
  <div class="tab">
    <svg width="10" height="20" viewBox="0 0 10 20"><rect x="1" y="1" width="8" height="18" rx="2" fill="#3d4244"/><circle cx="5" cy="6" r="1.5" fill="#fff"/><circle cx="5" cy="10" r="1.5" fill="#fff"/><circle cx="5" cy="14" r="1.5" fill="#fff"/></svg>Permission</div>
  <div class="tab">
    <svg width="22" height="18" viewBox="0 0 22 18" fill="none" stroke="#3d4244" stroke-width="1.4"><path d="M1 1v16h20M5 15V9M9 15V6M13 15V10M17 15V5M4 9l5-4 4 5 5-6"/></svg>Financial</div>
</nav>

<div class="field" style="left:18px;top:339px;width:376px"><div class="ico"><svg class="i" width="36" height="36" viewBox="0 0 36 36"><circle cx="18" cy="11" r="7"/><path d="M3 34v-4c0-6 7-9 15-9s15 3 15 9v4z"/></svg></div><span class="label">First Name</span></div>
<div class="field" style="left:411px;top:339px;width:377px"><div class="ico"><svg class="i" width="36" height="36" viewBox="0 0 36 36"><circle cx="18" cy="11" r="7"/><path d="M3 34v-4c0-6 7-9 15-9s15 3 15 9v4z"/></svg></div><span class="label">Last Name</span></div>
<div class="field" style="left:804px;top:339px;width:378px"><div class="ico"><svg class="i" width="36" height="36" viewBox="0 0 36 36"><path d="M18 3c-2 3 0 5 0 5s2-2 0-5zM18 8v5M8 13h20v7H8zM6 20h24v8H6zM2 33h32M8 17c3 2 5-2 10 0s7-2 10 0"/></svg></div><span class="label">Year of Birth</span></div>

<div class="field" style="left:18px;top:427px;width:1166px"><div class="ico"><svg class="i" width="40" height="38" viewBox="0 0 40 38"><path d="M20 26s-8-9-8-15a8 8 0 0 1 16 0c0 6-8 15-8 15z"/><circle cx="20" cy="11" r="3"/><path d="M13 22H5l-3 13h36l-3-13h-8"/></svg></div><span class="label">Address</span></div>

<div class="field" style="left:18px;top:515px;width:575px"><div class="ico"><svg width="28" height="28" viewBox="0 0 28 28" fill="none" stroke="var(--icon)" stroke-width="1.6"><rect x="2" y="2" width="6" height="5" fill="var(--icon)"/><rect x="11" y="11" width="6" height="5" fill="var(--icon)"/><rect x="20" y="20" width="6" height="5"/><path d="M5 7v6h6M14 16v6h6"/></svg></div><span class="label">Suburb</span></div>
<div class="field" style="left:610px;top:515px;width:574px"><div class="ico"><svg width="40" height="24" viewBox="0 0 40 24"><rect x="1" y="1" width="38" height="22" rx="4" fill="none" stroke="var(--icon)" stroke-width="1.6"/><text x="20" y="18" text-anchor="middle" font-family="Roboto,sans-serif" font-size="16" fill="var(--icon)">ZIP</text></svg></div><span class="label">Post Code</span></div>

<div class="field" style="left:18px;top:603px;width:376px"><div class="ico"><svg class="i" width="36" height="26" viewBox="0 0 36 26"><rect x="1" y="1" width="34" height="24"/><path d="M1 1l17 14L35 1M1 25l13-12M35 25L22 13"/></svg></div><span class="label">Email</span></div>
<div class="field" style="left:411px;top:603px;width:377px"><div class="ico"><svg class="i" width="22" height="36" viewBox="0 0 22 36"><rect x="2" y="1" width="18" height="34" rx="2"/><path d="M2 6h18M2 28h18"/><circle cx="11" cy="31.5" r="1.3" fill="var(--icon)"/></svg></div><span class="label">Mobile</span></div>
<div class="field" style="left:804px;top:603px;width:378px"><div class="ico"><svg class="i" width="34" height="34" viewBox="0 0 34 34"><path d="M8 2l5 7-3 3c2 5 6 9 11 11l3-3 7 5-4 6C15 30 4 19 2 6z"/><path d="M20 8a6 6 0 0 1 6 6M20 3a11 11 0 0 1 11 11"/></svg></div><span class="label">Landline</span></div>

<h2 class="section-title" style="font-weight:400">Emergency Contact</h2>

<div class="field" style="left:18px;top:788px;width:376px"><div class="ico"><svg class="i" width="36" height="36" viewBox="0 0 36 36"><circle cx="18" cy="11" r="7"/><path d="M3 34v-4c0-6 7-9 15-9s15 3 15 9v4z"/></svg></div><span class="label">First Name</span></div>
<div class="field" style="left:411px;top:788px;width:377px"><div class="ico"><svg class="i" width="36" height="36" viewBox="0 0 36 36"><circle cx="18" cy="11" r="7"/><path d="M3 34v-4c0-6 7-9 15-9s15 3 15 9v4z"/></svg></div><span class="label">Last Name</span></div>
<div class="field" style="left:804px;top:788px;width:378px"><div class="ico"><svg width="34" height="32" viewBox="0 0 34 32" fill="var(--icon)"><circle cx="7" cy="5" r="4"/><circle cx="27" cy="5" r="4"/><path d="M1 16c0-4 3-6 6-6s6 2 6 6zM21 16c0-4 3-6 6-6s6 2 6 6z"/><circle cx="17" cy="19" r="4"/><path d="M11 31c0-4 3-6 6-6s6 2 6 6z"/><path d="M7 16v4h6M27 16v4h-6" fill="none" stroke="var(--icon)" stroke-width="1.4"/></svg></div><span class="label">Relationship</span></div>

<div class="field" style="left:18px;top:876px;width:1166px"><div class="ico"><svg class="i" width="36" height="36" viewBox="0 0 36 36"><circle cx="18" cy="11" r="7"/></svg></div></div>
</body>
</html>
```